Conveyancing flyer

We need a flyer design for a new service we are offering. Dwellquarter.co.uk is launching its own conveyancing business called Keystone Counsel.

It has a strapline of 'Committed to helping you move'

Bullet points of the key features of the service are:-

* Hand-picked team of expert lawyers
• Fixed fees
• Capacity management
• Faster times to exchange of contracts
• More certainty and less stress

We need a large call now area and it should fit our branding which you can within our website, in particular with the colours of our logo.

Ideally we would like an area on the back to summarise the service in a little more details. So would need a text area as will. This area would be labelled 'Taking the guesswork out of dining the right lawyer'

The flyer should be double sized and a5

Please note this requirement is an A5 flyer double sided, not just the front. Please resubmit if you have designed differently.

```html
<!DOCTYPE html>
<html lang="en">
<head>
<meta charset="utf-8">
<title>Dwellquarter.co.uk – Keystone Counsel flyer</title>
<link href="https://fonts.googleapis.com/css2?family=Archivo+Black&family=Roboto:wght@300;400;700&display=swap" rel="stylesheet">
<style>
  :root {
    --backdrop: #c6c6c6;
    --paper: #ffffff;
    --magenta: #e5097f;
    --ink: #111111;
    --grey-line: #bdbdbd;
    --logo-grey: #7a7a7a;
    --footer: #000000;
    --web-green: #6fc02f;
    --photo-light: #f6f3ee;
    --photo-warm: #d9b98c;
  }
  * { margin: 0; padding: 0; box-sizing: border-box; }
  html, body { width: 1200px; height: 857px; overflow: hidden; }
  body {
    background: var(--backdrop);
    font-family: "Roboto", Arial, sans-serif;
    color: var(--ink);
    position: relative;
  }
  .flyer {
    position: absolute;
    top: 36px;
    width: 555px;
    height: 780px;
    background: var(--paper);
    box-shadow: 3px 3px 4px rgba(0,0,0,0.35);
    overflow: hidden;
  }
  .flyer--front { left: 27px; }
  .flyer--back { left: 613px; }

  /* header */
  .masthead { position: absolute; left: 0; top: 0; width: 555px; height: 112px; }
  .masthead__frame { position: absolute; left: 0; top: 0; }
  .brand { position: absolute; left: 19px; top: 24px; }
  .brand__name {
    display: flex; align-items: center; gap: 8px;
    font-family: "Roboto", Arial, sans-serif;
    font-weight: 300; font-size: 30px; line-height: 1;
    color: var(--logo-grey); letter-spacing: -0.5px;
  }
  .brand__mark { width: 20px; height: 20px; background: var(--magenta); }
  .brand__tagline {
    margin-top: 14px;
    font-family: "Roboto", Arial, sans-serif;
    font-weight: 400; font-size: 12.5px; color: var(--magenta);
  }
  .callout {
    position: absolute; left: 330px; top: 36px; width: 164px;
    text-align: center;
  }
  .callout__cta { font-family: "Archivo Black", Arial, sans-serif; font-size: 17px; line-height: 1; }
  .callout__free { font-family: "Roboto", Arial, sans-serif; font-weight: 700; font-size: 10.5px; margin-top: 3px; letter-spacing: 0.3px; }
  .callout__number { font-family: "Archivo Black", Arial, sans-serif; font-size: 21px; margin-top: 7px; white-space: nowrap; }

  /* front */
  .launch {
    position: absolute; left: 33px; top: 163px; width: 522px; height: 90px;
    background: var(--magenta); padding: 8px 0 0 13px;
  }
  .launch__intro { font-family: "Archivo Black", Arial, sans-serif; font-size: 20px; color: var(--ink); line-height: 1.1; }
  .launch__title { font-family: "Archivo Black", Arial, sans-serif; font-size: 39px; color: #fff; line-height: 1.2; margin-top: 2px; }
  .strapline {
    position: absolute; left: 46px; top: 300px;
    font-family: "Archivo Black", Arial, sans-serif; font-size: 23px; line-height: 1;
  }
  .features { position: absolute; left: 49px; top: 340px; list-style: none; }
  .features li {
    font-weight: 300; font-size: 22px; line-height: 31.3px; white-space: nowrap;
  }
  .features li::before { content: "•"; font-weight: 700; margin-right: 12px; }
  .hero-photo {
    position: absolute; left: 0; top: 495px; width: 555px; height: 221px;
    background: linear-gradient(180deg, var(--photo-light) 0%, #f1e7da 45%, var(--photo-warm) 100%);
  }

  /* back */
  .summary {
    position: absolute; left: 0; top: 111px; width: 555px; height: 389px;
    background: var(--magenta); color: #fff; padding: 22px 40px 0 30px;
  }
  .summary__title { font-family: "Archivo Black", Arial, sans-serif; font-size: 25.5px; line-height: 33px; }
  .summary__body { margin-top: 14px; font-weight: 400; font-size: 12.3px; line-height: 15.7px; }
  .reasons { position: absolute; left: 30px; top: 523px; width: 510px; }
  .reasons__title { font-family: "Roboto", Arial, sans-serif; font-weight: 700; font-size: 13.5px; margin-bottom: 4px; }
  .reasons__list { list-style: none; }
  .reasons__list li { font-size: 11px; line-height: 18.2px; white-space: nowrap; }
  .reasons__list li::before { content: "•"; margin-right: 5px; }

  /* footer */
  .footer-rule { position: absolute; left: 0; top: 716px; width: 555px; height: 8px; background: var(--grey-line); }
  .footer {
    position: absolute; left: 0; top: 724px; width: 555px; height: 56px;
    background: var(--footer); text-align: center; padding-top: 10px;
  }
  .footer__address { color: #fff; font-size: 11px; line-height: 1.3; }
  .footer__web { color: var(--web-green); font-family: "Roboto", Arial, sans-serif; font-weight: 700; font-size: 14.5px; margin-top: 2px; }
</style>
</head>
<body>

<section class="flyer flyer--front">
  <header class="masthead">
    <svg class="masthead__frame" width="555" height="112" viewBox="0 0 555 112">
      <polyline points="0,108 327,108 327,49 293,49 433,12 533,49 533,108 555,108" fill="none" stroke="#bdbdbd" stroke-width="6" stroke-linejoin="miter"/>
    </svg>
    <div class="brand">
      <div class="brand__name"><span class="brand__mark"></span>dwellquarter.co.uk</div>
      <div class="brand__tagline">The UK's Biggest &amp; Best Online Estate Agent</div>
    </div>
    <div class="callout">
      <div class="callout__cta">CALL US NOW</div>
      <div class="callout__free">FREEPHONE</div>
      <div class="callout__number">0808 555 0142</div>
    </div>
  </header>

  <div class="launch">
    <p class="launch__intro">Introducing our new service</p>
    <h1 class="launch__title">Keystone Counsel</h1>
  </div>

  <h2 class="strapline">Committed to helping you move</h2>
  <ul class="features">
    <li>Hand-picked team of expert lawyers</li>
    <li>Fixed fees</li>
    <li>Capacity management</li>
    <li>Faster times to exchange of contracts</li>
    <li>More certainty and less stress</li>
  </ul>

  <div class="hero-photo" role="img" aria-label="Smiling family of four holding cardboard moving boxes"></div>

  <div class="footer-rule"></div>
  <footer class="footer">
    <p class="footer__address">Address: Estate Offices, Units 7 &amp; 7a, Marlow Park Road, Brentwick, Essex CM9 2QX</p>
    <p class="footer__web">www.dwellquarter.co.uk</p>
  </footer>
</section>

<section class="flyer flyer--back">
  <header class="masthead">
    <svg class="masthead__frame" width="555" height="112" viewBox="0 0 555 112">
      <polyline points="0,108 327,108 327,49 293,49 433,12 533,49 533,108 555,108" fill="none" stroke="#bdbdbd" stroke-width="6" stroke-linejoin="miter"/>
    </svg>
    <div class="brand">
      <div class="brand__name"><span class="brand__mark"></span>dwellquarter.co.uk</div>
      <div class="brand__tagline">The UK's Biggest &amp; Best Online Estate Agent</div>
    </div>
    <div class="callout">
      <div class="callout__cta">CALL US NOW</div>
      <div class="callout__free">FREEPHONE</div>
      <div class="callout__number">0808 555 0142</div>
    </div>
  </header>

  <div class="summary">
    <h2 class="summary__title">Taking the guesswork out of<br>dining the right lawyer.</h2>
    <p class="summary__body">Lorem ipsum dolor sit amet, magna ac nulla lorem, ac lacinia sapien eu, montes lorem vel et, aliquam sed integer arcu arcu pede. Dignissim fermentum adipiscing etiam, pellentesque vehicula nunc blandit. Vestibulum per, condimentum duis hac vitae rutrum phasellus. Ac dapibus potenti donec. Tellus justo arcu eleifend, ligula morbi pretium nec, semper eget praesent, suspendisse curabitur bibendum. Sit lacus, mauris eros aliquet leo ut nibh, nonummy et ante in volutpat diam, mollis morbi ipsum eget dictum inceptos. In vivamus mauris arcu sodales fermentum duis, sed nulla orci urna totam suspendisse in, neque dictumst placerat tincidunt fermentum. Nullam amet quis enim et. Rutrum diam eleifend quis in dolor tincidunt.<br>
    Dui ligula aliquet tortor ultrices, elit est temporibus lobortis ultricies dapibus. Fames magnis tortor maecenas, sem quis cubilia, faucibus nibh rhoncus donec vitae, purus egestas ultricies sit imperdiet, risus luctus dictumst mi. Nec tortor donec, consectetur imperdiet nonummy nisl sed, vehicula nam enim fringilla sit, nibh maecenas, id ante inceptos nulla et porttitor. Nam dui at suspendisse wisi, ut mi mi, sodales integer tincidunt pellentesque ipsum, vel sit mauris mi. Arcu enim tempor aliquam natoque cras wisi, erat sit nunc ac curabitur donec laborum, et in tortor auctor in. Nunc malesuada et. Sed morbi diam sodales id.</p>
  </div>

  <div class="reasons">
    <h3 class="reasons__title">Why are we So Good?</h3>
    <ul class="reasons__list">
      <li>An Internet, email, telephone and post based service</li>
      <li>Clear and independent professional advice is provided in plain English</li>
      <li>There are no surprises - fixed fee guarantee - our fees will not change unless your instructions do</li>
      <li>No move - no legal fee - If your move doesn't go ahead you won't have to pay any legal fees</li>
      <li>Our own dedicated team assisting through to completion day</li>
      <li>Open 7 days a week</li>
      <li>24/7 access to eTrack - our online case management tool - speeding up exchange</li>
      <li>Choose from two payment options for total flexiblity</li>
    </ul>
  </div>

  <div class="footer-rule"></div>
  <footer class="footer">
    <p class="footer__address">Address: Estate Offices, Units 7 &amp; 7a, Marlow Park Road, Brentwick, Essex CM9 2QX</p>
    <p class="footer__web">www.dwellquarter.co.uk</p>
  </footer>
</section>

</body>
</html>
```